Firma: Spirituosen Großhandel
Zielgruppe: Junge
Produkt: Gin 40%, 0,7L
Marke: Lumo GIN oder 23M GIN (23 mixed herbal components)
Ursprung: Deutschland
Geschmack: frisch, mild, geschmeidig und weich
Der Gin könnten zwei Idee sein.
1. Lumo Gin, da der Geschmack frisch, mild, rein ist.
2. 23M Gin, da der aus 18 verschiedenen Pflanzen destilliert wird. (englich. 23 Mixed Pflanzen bzw. 23M)
Wacholder, Zitrusfrüchte, Ingwer, Kirschblüte, schwarzer Pfeffer, Minze, grüner Tee, Grapefruit usw.
Seite: Vor-, Rückseite und Kapsel/Halsetikett
Material: Papier oder Plastikfolie
Art: modern oder klassisch, hochwertig und Auffällig!!!
Flaschtyp: 2 Glass Durchsichtig (im Anhang)
Eigenschaften: Fluoreszierender Teil auf dem Etikett
Hochwertig wegen Primium Qualität
Flasche und Etikett passen miteinander

```html
<!DOCTYPE html>
<html lang="de">
<head>
<meta charset="utf-8">
<title>Lumo GIN – Etiketten</title>
<link href="https://fonts.googleapis.com/css2?family=Playfair+Display:wght@500&family=Cormorant+Garamond:wght@500&family=Fira+Sans+Condensed:wght@300&family=Oswald:wght@300&display=swap" rel="stylesheet">
<style>
  :root {
    --bg-top: #979ea5;
    --bg-bottom: #c2c3c4;
    --paper: #f8f5ec;
    --paper-line: rgba(200, 190, 165, 0.12);
    --ink-blue: #1f6c99;
    --ink-grey: #5b5b5b;
    --dot: #9a9a9a;
    --wave-light: #a9cde3;
    --wave-deep: #4b8fbd;
  }
  * { margin: 0; padding: 0; box-sizing: border-box; }
  html, body { width: 1200px; height: 2400px; overflow: hidden; }
  body {
    background: linear-gradient(180deg, var(--bg-top) 0%, var(--bg-bottom) 100%);
    position: relative;
    font-family: "Cormorant Garamond", serif;
  }
  .label {
    position: absolute;
    background-color: var(--paper);
    background-image: repeating-linear-gradient(90deg, transparent 0 6px, var(--paper-line) 6px 7px);
  }
  .label--front {
    left: 94px; top: 850px; width: 563px; height: 689px;
    clip-path: polygon(0 0, 563px 0, 515px 689px, 51px 689px);
  }
  .label--back {
    left: 777px; top: 850px; width: 330px; height: 695px;
    clip-path: polygon(0 0, 330px 0, 281px 695px, 48px 695px);
  }
  .label__frame { position: absolute; inset: 0; }
  .label__frame line { stroke: var(--dot); stroke-width: 1.6; stroke-dasharray: 1.6 6; stroke-linecap: round; }
  .tagline {
    position: absolute; left: 0; right: 0; text-align: center;
    font-family: "Playfair Display", serif; font-weight: 500;
    color: var(--ink-grey); letter-spacing: 0.22em; text-transform: uppercase;
  }
  .label--front .tagline { top: 66px; font-size: 19px; }
  .label--back .tagline { top: 124px; font-size: 15px; line-height: 22px; letter-spacing: 0.16em; }
  .ship-art {
    position: absolute;
    background: radial-gradient(ellipse at 50% 60%, var(--ink-blue) 0%, #3f86b4 55%, rgba(63,134,180,0) 75%);
  }
  .label--front .ship-art { left: 230px; top: 152px; width: 137px; height: 92px; }
  .label--back .ship-art { left: 138px; top: 61px; width: 68px; height: 58px; }
  .brand {
    position: absolute; left: 0; right: 0; text-align: center;
    font-family: "Playfair Display", serif; font-weight: 500; color: var(--ink-blue);
  }
  .brand__word { display: block; text-transform: uppercase; }
  .label--front .brand { top: 258px; }
  .label--front .brand__word--small { font-size: 34px; letter-spacing: 0.6em; padding-left: 0.6em; line-height: 40px; }
  .label--front .brand__word--large { font-size: 118px; line-height: 112px; letter-spacing: 0.01em; }
  .label--back .brand { top: 192px; }
  .label--back .brand__word--small { font-size: 19px; letter-spacing: 0.55em; padding-left: 0.55em; line-height: 24px; }
  .label--back .brand__word--large { font-size: 62px; line-height: 60px; }
  .flavour {
    position: absolute; left: 0; right: 0; top: 444px; text-align: center;
    font-family: "Fira Sans Condensed", sans-serif; font-weight: 300;
    font-size: 17px; line-height: 23px; letter-spacing: 0.14em; color: var(--ink-grey);
  }
  .wave-band {
    position: absolute;
    background: linear-gradient(180deg, rgba(169,205,227,0.2) 0%, var(--wave-light) 35%, var(--wave-deep) 60%, var(--wave-light) 85%, rgba(169,205,227,0.2) 100%);
  }
  .label--front .wave-band { left: 38px; width: 488px; top: 529px; height: 104px; }
  .label--back .wave-band { left: 40px; width: 250px; top: 533px; height: 72px; }
  .spec {
    position: absolute; top: 634px;
    font-family: "Playfair Display", serif; font-weight: 500; font-size: 34px; color: var(--ink-blue);
  }
  .spec--abv { left: 81px; }
  .spec--volume { left: 414px; }
  .body-copy {
    position: absolute; left: 60px; right: 60px; top: 318px; text-align: center;
    font-family: "Oswald", sans-serif; font-weight: 300;
    font-size: 15px; line-height: 23px; color: var(--ink-grey);
  }
  .foot-copy {
    position: absolute; left: 0; right: 0; top: 620px; text-align: center;
    font-family: "Oswald", sans-serif; font-weight: 300; font-size: 15px; color: var(--ink-grey);
  }
</style>
</head>
<body>

  <section class="label label--front" aria-label="Vorderetikett">
    <svg class="label__frame" width="563" height="689" viewBox="0 0 563 689" aria-hidden="true">
      <line x1="55" y1="20" x2="510" y2="20"/>
      <line x1="29" y1="44" x2="57" y2="484"/>
      <line x1="540" y1="44" x2="507" y2="484"/>
      <line x1="205" y1="657" x2="380" y2="657"/>
    </svg>
    <p class="tagline">Deutsches Premiumprodukt</p>
    <div class="ship-art" role="img" aria-label="Illustration eines Segelschiffs auf Wellen"></div>
    <h1 class="brand"><span class="brand__word brand__word--small">Lumo</span><span class="brand__word brand__word--large">GIN</span></h1>
    <p class="flavour">Frisch, mild und geschmeidig<br>weich im Geschmack</p>
    <div class="wave-band" role="img" aria-label="Dekoratives Wellenmuster in Blautönen"></div>
    <span class="spec spec--abv">40 %</span>
    <span class="spec spec--volume">0,7 l</span>
  </section>

  <section class="label label--back" aria-label="Rückenetikett">
    <svg class="label__frame" width="330" height="695" viewBox="0 0 330 695" aria-hidden="true">
      <line x1="43" y1="17" x2="277" y2="17"/>
      <line x1="26" y1="26" x2="56" y2="481"/>
      <line x1="303" y1="26" x2="277" y2="481"/>
      <line x1="85" y1="660" x2="265" y2="660"/>
    </svg>
    <div class="ship-art" role="img" aria-label="Kleine Illustration eines Segelschiffs"></div>
    <p class="tagline">Deutsches<br>Premiumprodukt</p>
    <h2 class="brand"><span class="brand__word brand__word--small">Lumo</span><span class="brand__word brand__word--large">GIN</span></h2>
    <p class="body-copy">Lorem ipsum dolor sit amet, consectetuer adipiscing elit, sed diam nonummy nibh euismod tincidunt ut laoreet dolore magna aliquam erat volutpat. Ut wisi enim ad minim.</p>
    <div class="wave-band" role="img" aria-label="Dekoratives Wellenmuster in Blautönen"></div>
    <p class="foot-copy">Lorem ipsum dolor sit amet,</p>
  </section>

</body>
</html>
```